Elegant Business Cards & Letterhead

We will need the following that need to be designed: Letterhead and Business Cards, there winer will be re-hired for the balance of our stationary needs. Text for the cards and letterheads:

- Corporate Card instead of name
- landline: +971 (4) 362 7041
- mobile: +971 56 2819 605
- 800TUTOR
- email: dubai@velmora-lune.com
- www.velmora-lune.com
- PO Box 387261
Address: Castellan Heights Suite 1708, Dubai UAE

Thank you

Target Market(s)

VIPs, HNWI, High-end Families.

Industry/Entity Type

Luxury Market

Font styles to use
Other font styles liked:
• as explained

Colors

Designer to choose only greyscale colors for use in the design.

Requirements
Must have
• Elegant, Simple, Luxurious, Minimalistic
Nice to have
• Luxury, Golds, Engravings,
Should not have
• Much colors, funky,

```html
<!DOCTYPE html>
<html lang="en">
<head>
<meta charset="utf-8">
<title>Velmora Lune — Business Cards</title>
<link rel="stylesheet" href="https://fonts.googleapis.com/css2?family=Marcellus&family=Open+Sans:wght@400;600&display=swap">
<style>
  :root {
    --backdrop: #7f9bbd;
    --paper: #ffffff;
    --plum: #3b2430;
    --ink: #2e1a24;
    --band-text: #f4ece6;
    --gold-deep: #8a5a26;
    --gold-mid: #c89a4e;
    --gold-light: #efe3a2;
    --gold-sheen: linear-gradient(100deg, var(--gold-deep) 0%, var(--gold-mid) 30%, var(--gold-light) 55%, var(--gold-mid) 78%, var(--gold-deep) 100%);
    --gold-face: linear-gradient(155deg, #c28d4c 0%, #e6cd8c 30%, #f1e4ac 50%, #e8c98a 72%, #c98a48 100%);
  }
  * { box-sizing: border-box; margin: 0; padding: 0; }
  html, body { width: 1200px; height: 876px; overflow: hidden; }
  body {
    background: var(--backdrop);
    display: flex;
    align-items: center;
    justify-content: center;
    gap: 40px;
    font-family: "Open Sans", Arial, sans-serif;
  }
  .card {
    position: relative;
    width: 540px;
    height: 309px;
    overflow: hidden;
    box-shadow: 0 10px 24px rgba(30, 45, 75, 0.35);
  }

  /* Front */
  .card-front { background: var(--paper); }
  .top-rule {
    position: absolute; top: 0; left: 0; right: 0; height: 20px;
    display: flex; align-items: center;
  }
  .top-rule .rule-short { width: 34px; height: 100%; background: var(--gold-sheen); }
  .top-rule .rule-long { flex: 1; height: 100%; background: var(--gold-sheen); }
  .top-rule .brand-small {
    font-family: "Marcellus", Georgia, serif;
    font-size: 19px; letter-spacing: 0.5px;
    color: var(--ink);
    padding: 0 12px;
    margin-top: 22px;
    white-space: nowrap;
  }
  .identity {
    position: absolute; top: 108px; left: 0; right: 0;
    text-align: center;
  }
  .identity .brand-name {
    font-family: "Marcellus", Georgia, serif;
    font-size: 26px; color: var(--ink); letter-spacing: 0.5px;
  }
  .identity .role {
    font-size: 11px; color: var(--ink); margin-top: -2px;
  }
  .contact-band {
    position: absolute; left: 0; right: 0; bottom: 46px; height: 30px;
    background: var(--plum);
    display: flex; align-items: center; gap: 22px;
    padding-left: 24px;
    color: var(--band-text); font-size: 12px;
    white-space: nowrap;
  }
  .address-band {
    position: absolute; left: 0; right: 0; bottom: 0; height: 46px;
    background: var(--gold-sheen);
    display: flex; align-items: flex-start; gap: 22px;
    padding: 7px 0 0 18px;
    color: var(--ink); font-size: 12px;
    white-space: nowrap;
  }
  .line-item { display: flex; align-items: center; gap: 6px; }
  .line-item svg { width: 11px; height: 11px; flex: none; }

  /* Back */
  .card-back { background: var(--gold-face); }
  .card-back .brand-large {
    position: absolute; top: 108px; left: 0; right: 0; text-align: center;
    font-family: "Marcellus", Georgia, serif;
    font-size: 52px; letter-spacing: 1px; color: var(--ink);
  }
  .card-back .web {
    position: absolute; top: 196px; left: 66px;
    font-size: 13px; letter-spacing: 7px; color: var(--ink);
  }
</style>
</head>
<body>

  <section class="card card-front" aria-label="Business card front">
    <div class="top-rule">
      <span class="rule-short"></span>
      <span class="brand-small">VELMORA LUNE</span>
      <span class="rule-long"></span>
    </div>

    <div class="identity">
      <p class="brand-name">VELMORA LUNE</p>
      <p class="role">Corporate Card</p>
    </div>

    <div class="contact-band">
      <span class="line-item">
        <svg viewBox="0 0 12 12" aria-hidden="true"><path fill="currentColor" d="M2.4 1h2l1 2.6-1.3 1a6.5 6.5 0 0 0 3.3 3.3l1-1.3 2.6 1v2c0 .8-.7 1.4-1.5 1.4A9.8 9.8 0 0 1 1 2.5C1 1.7 1.6 1 2.4 1z"/></svg>
        +971 (4) 362 7041
      </span>
      <span class="line-item">
        <svg viewBox="0 0 12 12" aria-hidden="true"><path fill="currentColor" d="M3.5 .5h5a1 1 0 0 1 1 1v9a1 1 0 0 1-1 1h-5a1 1 0 0 1-1-1v-9a1 1 0 0 1 1-1zm.5 1.5v6.5h4V2zm2 7.3a.7.7 0 1 0 0 1.4.7.7 0 0 0 0-1.4z"/></svg>
        +971 56 2819 605
      </span>
      <span class="line-item">
        <svg viewBox="0 0 12 12" aria-hidden="true"><path fill="currentColor" d="M2 1l9 4.5-4 1-1 4z"/></svg>
        dubai@velmora-lune.com
      </span>
    </div>

    <div class="address-band">
      <span class="line-item">
        <svg viewBox="0 0 12 12" aria-hidden="true"><path fill="currentColor" d="M6 .5a4 4 0 0 0-4 4c0 3 4 7 4 7s4-4 4-7a4 4 0 0 0-4-4zm0 5.5a1.5 1.5 0 1 1 0-3 1.5 1.5 0 0 1 0 3z"/></svg>
        Castellan Heights Suite 1708, PO Box 387261, Dubai UAE
      </span>
      <span class="line-item">
        <svg viewBox="0 0 12 12" aria-hidden="true"><path fill="currentColor" d="M2.4 1h2l1 2.6-1.3 1a6.5 6.5 0 0 0 3.3 3.3l1-1.3 2.6 1v2c0 .8-.7 1.4-1.5 1.4A9.8 9.8 0 0 1 1 2.5C1 1.7 1.6 1 2.4 1z"/></svg>
        800TUTOR
      </span>
    </div>
  </section>

  <section class="card card-back" aria-label="Business card back">
    <p class="brand-large">VELMORA LUNE</p>
    <p class="web">www.velmora-lune.com</p>
  </section>

</body>
</html>
```